Flyer-Design für Rücken-Massage, Klangtherapie etc.
Sehr kompetent und schnelle Umsetzung, gute Gestaltung, Farblich in Harmonie. Schnelle Änderungen, bin sehr zufrieden. Danke für die super Arbeit.
Zielgruppe
Rücken-Massage, Klangtherapie, Fußreflex-Massage, Quantenheilung
Aufgabenstellung
Text zu den Rubriken können vom Internet entnommen werden.
https://wohlruhe-praxis.ch/

```html
<!DOCTYPE html>
<html lang="de">
<head>
<meta charset="utf-8">
<title>Flyer – Wohlruhe Klangpraxis</title>
<link href="https://fonts.googleapis.com/css2?family=Montserrat:wght@400;500;600;700&display=swap" rel="stylesheet">
<style>
  :root {
    --paper: #ffffff;
    --ink: #1e1e1e;
    --brand-green: #8cc63f;
    --photo-green: #c9dd8e;
    --photo-skin: #ecc9b4;
    --photo-bronze: #b98b45;
    --photo-cloth: #6e3528;
  }
  * { margin: 0; padding: 0; box-sizing: border-box; }
  html, body { width: 846px; height: 1200px; overflow: hidden; background: var(--paper); }
  body { font-family: "Montserrat", sans-serif; color: var(--ink); }
  .flyer { position: relative; width: 846px; height: 1200px; background: var(--paper); }

  .brand { position: absolute; top: 40px; left: 345px; display: flex; align-items: center; gap: 16px; }
  .brand-dot { width: 64px; height: 64px; border-radius: 50%; background: var(--brand-green); flex: none; }
  .brand-name { color: var(--brand-green); font-weight: 500; font-size: 30px; line-height: 1.05; letter-spacing: -0.2px; }

  .section-title { position: absolute; font-weight: 600; font-size: 22px; line-height: 1.3; text-align: center; }
  .body-text { position: absolute; font-size: 16.6px; line-height: 22.4px; hyphens: auto; -webkit-hyphens: auto; }
  .body-text p + p { margin-top: 22px; }
  .justified { text-align: justify; }
  .centered { text-align: center; }

  .intro-title { top: 154px; left: 80px; width: 686px; }
  .intro-text { top: 234px; left: 118px; width: 650px; }

  .reflex-title { top: 448px; left: 80px; width: 686px; }
  .reflex-text { top: 488px; left: 78px; width: 690px; }
  .reflex-text-2 { top: 648px; left: 78px; width: 426px; }
  .reflex-photo { position: absolute; top: 612px; left: 520px; width: 273px; height: 180px;
    background: linear-gradient(120deg, var(--photo-green) 0%, #e8f0cf 45%, var(--photo-skin) 70%, #f6e6e8 100%); }

  .bowls-title { top: 870px; left: 80px; width: 310px; }
  .bowls-photo { position: absolute; top: 935px; left: 80px; width: 313px; height: 210px;
    background: linear-gradient(160deg, #d9a66a 0%, var(--photo-bronze) 40%, var(--photo-cloth) 100%); }
  .bowls-text { top: 883px; left: 416px; width: 382px; }
</style>
</head>
<body>
<main class="flyer">
  <header class="brand">
    <span class="brand-dot"></span>
    <div class="brand-name">Wohlruhe Klangpraxis<br>Lenora Tannhofer</div>
  </header>

  <h1 class="section-title intro-title">Viele Menschen leiden unter<br>Rückenschmerzen und -verspannungen.</h1>
  <div class="body-text centered intro-text">
    <p>Grund dafür ist oftmals Stress, Bewegungsmangel, langes Sitzen und schlechte Körperhaltung. Aber auch belastende Emotionen können für Verspannungen im Rücken sorgen. Eine Massage kann diese Schmerzen lindern und auch tiefe Verspannungen lockern. Zusätzlich wird durch die Berührung der positive Energiefluss angeregt, Alltagsprobleme treten in den Hintergrund und emotionale Blockaden werden gelöst.</p>
  </div>

  <h2 class="section-title reflex-title">Fussreflexzonenmassage</h2>
  <div class="body-text justified reflex-text">
    <p>Fussreflexzonenmassage ist eine Methode, mit welcher ich Ihre körpereigenen Heilungskräfte aktivieren werde. Von altertümlichen Texten, Illustrationen und Artefakten weiss man, dass die frühen chinesischen, japanischen, ägyptischen und indianischen Kulturen schon die Behandlung an den Füssen gefördert haben.</p>
  </div>
  <div class="body-text justified reflex-text-2">
    <p>Das Prinzip von der Fussreflexzonenmassage beruht auf der Erkenntnis, dass Energiezonen durch den Körper laufen. In den Füssen reflektieren sich diese Zonen und korrespondieren mit den wichtigen Organen, Drüsen und anderen Körperteilen.</p>
  </div>
  <div class="reflex-photo" role="img" aria-label="Foto: Hände massieren eine Fusssohle, daneben eine rosa Lilie vor grünem Hintergrund"></div>

  <h2 class="section-title bowls-title">Klangschalen</h2>
  <div class="bowls-photo" role="img" aria-label="Foto: Klangschalen aus Messing mit Klöppel auf einem braunen Tuch, weisse Orchidee im Hintergrund"></div>
  <div class="body-text justified bowls-text">
    <p>Durch die heilsamen Klänge werde ich Ihnen Ihre tiefsitzende Verspannungen lösen, wodurch die Selbstheilungskräfte Ihres Körpers freigesetzt und mobilisiert werden. Durch die Klangschalenmassage kann sehr schnell ein äusserst tiefer Entspannungszustand beim Behandelten erreicht werden. Die Töne der Klangschalen erinnern die Menschen an etwas ursprüngliches und Vertrautes und vermitteln dadurch ein entspannendes und wohliges Körpergefühl.</p>
  </div>
</main>
</body>
</html>
```